Web Design Project: Executive Coach

PLEASE check out http://tovrenly.com.sg/x/PixelHive/PixelHive_Brief/Blank.html

It is a better description of what I am after. It includes everything in this brief and in an easier format. (And...I don't have your design skills, so it doesn't look great.)

========

What the site offers
-
I am about to launch a one-person company that provides three services:
1) executive coaching
2) leadership training
3) psychotherapy to adults

My Unique Selling Point
-
My unique selling point is that I am a coach who is also a relatively senior psychologist. However, psychologists can be seen as scary and that may put people off.

The Biggest Challenge: The Target Audience
-
One challenge is that because I sell 3 services, I want to appeal to more than one demographic. They are:

1) The representative from HR of a company who wants to buy a leadership course or find a coach for an executive in the company. (Usually mid-40’s and older.)

2) The executives who will take the selection made by the head of HR and may choose me from 3 or 4 other options. (Usually late 30’s to mid 40’s. Both men and women. From multinational companies.)

3) Psychotherapy clients who are coming to be directly, not via HR, and who don’t want to feel insecure that they aren’t executives but still may be a good fit to work with me. (More women than men. Age 34-45. Typically have some European or American exposure.)

The Problem
-
The executives I see may or may not have some psychological concerns, but most will quite like that I am a psychologist as long as I’m not “scary” but “kind”. (Kind is key.) So while it is important to show I am a therapist, I don't want it to make executives embarrassed when a colleague says “Oh, I looked at this guy’s website. You aren't in therapy are you?”

As mentioned above, please check out the following link: http://tovrenly.com.sg/x/PixelHive/PixelHive_Brief/Blank.html

________
Please note, I originally posted this as 584207 Executive Coaching, Leadership Training, and Psychotherapy Website. With the help of one designer and also PixelHive customer support, I realized that I had requested only the design of a website, not the coding. I had offered the maximum amount, US$1000 (refundable). I am resubmitting the project here and I have guaranteed the funds. I am lowering the payment as I am now aware that I was only asking for design. I apologize for any inconvenience. And thank your for being interested in this project.
Updates

Project Deadline Extended
Reason: I would love to get started on the coding next week. So I hope to get your proposals in the next 3 days.

Target Market(s)

Primary audience: 34-44 year old men and women with some European / North American exposure

Industry/Entity Type

Leadership

Requirements
Must have
• Video on home page
Nice to have
• I would like have quotes slide in to a couple of the pages. These may have a photo of the author attached.

I would like Workvine integration with my business's Workvine page. (I haven't made one yet, so I'm not sure how it works.)

```html
<!DOCTYPE html>
<html lang="en">
<head>
<meta charset="utf-8">
<title>Tovrenly Consulting</title>
<link rel="stylesheet" href="https://fonts.googleapis.com/css2?family=Cinzel:wght@400;700&family=Open+Sans:wght@400;600&family=Crimson+Text:ital@1&display=swap">
<style>
:root{
  --grey:#e4e4e4;
  --white:#ffffff;
  --black:#0d0d0d;
  --orange:#f7931e;
  --ink:#1a1a1a;
  --text:#333333;
  --rule:#cfcfcf;
  --icon:#555555;
}
*{margin:0;padding:0;box-sizing:border-box}
html,body{width:705px;height:1200px;overflow:hidden}
body{position:relative;background:var(--white);font-family:"Open Sans",sans-serif;color:var(--text)}
h1,h2,h3,h4{font-weight:400}
.abs{position:absolute}

.site-header{left:0;top:0;width:705px;height:80px;background:var(--grey);text-align:center}
.brand{font-family:"Cinzel",serif;font-size:27px;color:var(--ink);letter-spacing:1px;padding-top:10px;line-height:34px}
.tagline{font-size:16px;color:#2b2b2b;margin-top:4px;letter-spacing:.3px}

.main-nav{left:0;top:82px;width:705px;height:38px;background:var(--black)}
.nav-item{position:absolute;top:0;height:38px;line-height:40px;font-family:"Cinzel",serif;font-size:12.5px;color:#fff;white-space:nowrap;letter-spacing:.2px}
.nav-item.active{top:2px;height:32px;line-height:34px;background:var(--orange);border-radius:2px;text-align:center}

.section-title{position:absolute;left:0;width:705px;text-align:center;font-family:"Cinzel",serif;color:var(--ink);line-height:26px}
.section-title span{background:var(--white);padding:0 18px;position:relative}
.rule{position:absolute;height:1px;background:var(--rule)}

.service{position:absolute;width:180px}
.service-tile{width:150px;height:127px;background:#e2e2e2;border:1px solid #d4d4d4}
.service-name{font-family:"Cinzel",serif;font-size:14.5px;color:var(--ink);margin-top:10px;letter-spacing:.3px;white-space:nowrap}
.service-desc{font-size:10.3px;line-height:17px;color:#111;margin-top:1px;width:175px;letter-spacing:-.1px}
.btn-more{position:absolute;width:83px;height:19px;border-radius:10px;background:var(--orange);color:#fff;font-size:9px;text-align:center;line-height:19px}

.profile{left:0;top:424px;width:705px;height:329px;background:var(--grey);text-align:center}
.profile-name{font-family:"Cinzel",serif;font-size:22px;color:var(--ink);margin-top:7px;letter-spacing:.5px;line-height:30px}
.profile-roles{font-size:11.5px;color:#222;margin-top:4px}
.network{font-size:19px;color:var(--ink);margin-top:6px}
.video-frame{left:162px;top:533px;width:380px;height:207px;border-radius:8px;background:linear-gradient(180deg,#cfcfcf 0%,#d9d3a8 35%,#c9c093 80%,#b8b8b8 100%)}

.testimonial{left:0;top:815px;width:705px;height:101px;background:var(--grey)}
.arrow{position:absolute;top:853px;width:17px;height:17px;border-radius:50%;background:#6b6b6b}
.avatar{left:58px;top:823px;width:80px;height:78px;border-radius:50%;background:radial-gradient(circle,#d9e2ea 0%,#c4cdd6 55%,#f4f4f4 58%,#ffffff 100%);border:1px solid #cccccc}
.quote{left:153px;top:842px;width:500px;font-family:"Crimson Text",serif;font-style:italic;font-size:12.6px;line-height:17px;color:#111;letter-spacing:-.1px}
.quote-author{left:550px;top:881px;font-size:11.5px;font-weight:600;color:#222}

.email-field{left:152px;top:980px;width:223px;height:31px;border:1px solid #c8c8c8;border-radius:3px;font-size:11px;color:#777;padding:7px 10px}
.btn-subscribe{left:388px;top:981px;width:151px;height:30px;background:var(--orange);color:#fff;font-size:14.5px;text-align:center;line-height:30px;border-radius:2px}

.site-footer{left:0;top:1050px;width:705px;height:120px;background:var(--grey);border-top:2px solid #d6d6d6}
.footer-title{position:absolute;font-family:"Cinzel",serif;font-weight:700;font-size:12.5px;color:var(--ink);white-space:nowrap}
.footer-text{position:absolute;font-size:9px;line-height:13px;color:#111}
.social{position:absolute;top:1088px;width:17px;height:17px;border-radius:50%;background:var(--icon)}
.btn-book{left:367px;top:1113px;width:118px;height:22px;background:var(--orange);color:#fff;font-size:9px;text-align:center;line-height:22px}
.copyright{left:0;top:1170px;width:705px;height:30px;background:#161616;color:#fff;font-size:9px;text-align:center;line-height:30px}
</style>
</head>
<body>

<header class="abs site-header">
  <h1 class="brand">Tovrenly Consulting</h1>
  <p class="tagline">TRANSFORMING TEAMS, LEADERS, AND INDIVIDUALS</p>
</header>

<nav class="abs main-nav">
  <span class="nav-item active" style="left:30px;width:156px">COACHING TRAINING</span>
  <span class="nav-item" style="left:202px">PSYCHOTHERAPY</span>
  <span class="nav-item" style="left:336px">FAQ</span>
  <span class="nav-item" style="left:387px">PUBLICATIONS</span>
  <span class="nav-item" style="left:506px">CLIENTS</span>
  <span class="nav-item" style="left:585px">CONTACT US</span>
</nav>

<div class="rule" style="left:20px;top:142px;width:665px"></div>
<h2 class="section-title" style="top:128px;font-size:19px"><span>My Expertise</span></h2>

<div class="service" style="left:36px;top:168px">
  <div class="service-tile" role="img" aria-label="Icon of a speaker at a lectern" style="margin-left:5px"></div>
  <h3 class="service-name">Leadership Training</h3>
  <p class="service-desc">Creating custom-made leadership workshops to fit the needs of organizations</p>
</div>
<div class="btn-more" style="left:68px;top:382px">KNOW MORE</div>

<div class="service" style="left:276px;top:168px">
  <div class="service-tile" role="img" aria-label="Icon of a coach at a board with two people" style="margin-left:2px"></div>
  <h3 class="service-name">ExecutiveCoaching</h3>
  <p class="service-desc">Partnering with clients one-on-one to actualize their professional potential</p>
</div>
<div class="btn-more" style="left:307px;top:382px">KNOW MORE</div>

<div class="service" style="left:516px;top:168px">
  <div class="service-tile" role="img" aria-label="Icon of a person reclining on a couch"></div>
  <h3 class="service-name" style="margin-left:16px">psychotherapy</h3>
  <p class="service-desc" style="margin-left:8px;width:160px">Deepening personal insight and developing behaviors to grow in well-being</p>
</div>
<div class="btn-more" style="left:556px;top:381px">KNOW MORE</div>

<section class="abs profile">
  <h2 class="profile-name">Dr. Julian Tovren</h2>
  <p class="profile-roles">EXECUTIVE COACH, LEADERSHIP TRAINER, ASST. PROFESSOR OF LEADERSHIP STUDIES, PSYCHOLOGIST</p>
  <p class="network">Join My Workvine Network</p>
</section>
<div class="abs video-frame" role="img" aria-label="Introductory video of the coach shown in a laptop screen"></div>

<div class="rule" style="left:18px;top:784px;width:669px"></div>
<h2 class="section-title" style="top:770px;font-size:19px"><span>What Our Customers Say About Us</span></h2>

<section class="abs testimonial"></section>
<div class="arrow" style="left:26px"></div>
<div class="arrow" style="left:662px"></div>
<div class="abs avatar" role="img" aria-label="Customer avatar"></div>
<p class="abs quote">It's pretty clear how awesome our work is. Think of how easy it'd be to sell it to others who could use it.<br>Awesome rates for selling even awesome services. I Really Like the way he had worked&nbsp; with us.</p>
<p class="abs quote-author">Mark</p>

<div class="rule" style="left:14px;top:946px;width:677px"></div>
<h2 class="section-title" style="top:933px;font-size:18px"><span>Sign Up For Weekly Newsletters</span></h2>
<div class="abs email-field">Enter Your Email address</div>
<div class="abs btn-subscribe">SUBSCRIBE NOW</div>

<footer class="abs site-footer"></footer>
<h4 class="footer-title" style="left:31px;top:1063px">About&nbsp; Tovrenly Consulting</h4>
<p class="footer-text" style="left:31px;top:1083px;width:290px;text-align:justify">He is Assistant Professor of Leadership Studies at the Harbourview School of Public Policy (the top ranked public policy school in Asia) which is located in the Northbridge University of Singapore (25th in World University Rankings). Dr. Tovren works with policy makers from more than 50 countries.</p>
<h4 class="footer-title" style="left:365px;top:1063px">We Are Socail</h4>
<span class="social" style="left:367px"></span>
<span class="social" style="left:391px"></span>
<span class="social" style="left:415px"></span>
<span class="social" style="left:438px"></span>
<div class="abs btn-book">BOOK AN APPOINTMENT</div>
<h4 class="footer-title" style="left:513px;top:1063px">Contact Us</h4>
<p class="footer-text" style="left:514px;top:1085px">Tovrenly Consulting<br>Kelvara Road<br>Singapore</p>

<div class="abs copyright">Copyright 2013 Tovrenly Consulting All Rights Reserved.</div>

</body>
</html>
```